flat share room mate rental website(design only)

We need a design for the homepage of a flat share / roommate website. We have a website template http://demo1.hometemplix.net and we're looking for a homepage similar to this http://uk.bunkpalora.com but different.
The main user of the site are likely to be students and young professionals so were not looking for anything too serious.
We want to emphasise that the website will be 100% free to use both to post an advert and to contact the advertiser.
We must have a 'new rooms' and new flatmates carousel, also we would prefer if the menu had only a login button and maybe a 'post a room' button.
Our logo is currently being designed, so you can put anything in its place.
We look forward to seeing what you guys come up with.
Target Market(s)
Students, Young Professionals
Industry/Entity Type
Rental
Number of Pages Required
1 page
Look and feel
Each slider illustrates characteristics of the customer's brand and the style your logo design should communicate.

```html
<!DOCTYPE html>
<html lang="en">
<head>
<meta charset="utf-8">
<title>Find your perfect flatmate</title>
<link href="https://fonts.googleapis.com/css2?family=Fira+Sans:wght@400;500&display=swap" rel="stylesheet">
<style>
  :root {
    --teal: #88cfc4;
    --pink: #f59195;
    --blue: #85c8e4;
    --grey: #dddddd;
    --white: #ffffff;
    --ink: #111111;
    --shade: rgba(28, 28, 28, 0.7);
    --arrow-pink: rgba(240, 140, 145, 0.85);
    --arrow-blue: rgba(120, 185, 215, 0.85);
    --room-photo:
      radial-gradient(ellipse 12% 22% at 26% 52%, rgba(235, 245, 225, 0.95) 0%, rgba(120, 170, 90, 0.8) 55%, rgba(120, 170, 90, 0) 100%),
      radial-gradient(ellipse 10% 8% at 28% 33%, rgba(185, 40, 90, 0.9) 0%, rgba(185, 40, 90, 0) 100%),
      radial-gradient(ellipse 11% 9% at 29% 66%, rgba(200, 40, 100, 0.9) 0%, rgba(200, 40, 100, 0) 100%),
      radial-gradient(ellipse 9% 8% at 65% 45%, rgba(255, 225, 160, 0.95) 0%, rgba(255, 225, 160, 0) 100%),
      radial-gradient(ellipse 35% 28% at 72% 80%, rgba(30, 22, 20, 0.95) 0%, rgba(30, 22, 20, 0) 100%),
      radial-gradient(ellipse 16% 22% at 50% 78%, rgba(130, 25, 55, 0.85) 0%, rgba(130, 25, 55, 0) 100%),
      radial-gradient(ellipse 18% 12% at 10% 76%, rgba(235, 225, 215, 0.8) 0%, rgba(235, 225, 215, 0) 100%),
      linear-gradient(180deg, #e6d6b0 0%, #c4ad74 22%, #a89463 50%, #6d5a42 78%, #2e2520 100%);
  }
  * { box-sizing: border-box; margin: 0; padding: 0; }
  html, body { width: 1200px; height: 2496px; overflow: hidden; }
  body { position: relative; background: var(--grey); font-family: "Fira Sans", "Trebuchet MS", sans-serif; color: var(--ink); }

  .site-header { position: absolute; left: 0; top: 0; width: 1200px; height: 85px; background: var(--teal); }
  .brand { position: absolute; left: 100px; top: 14px; display: flex; align-items: center; gap: 10px; }
  .brand-mark { width: 58px; height: 58px; border-radius: 50%; background: var(--white); }
  .brand-name { color: var(--white); font-size: 30px; font-weight: 500; }
  .nav-button { position: absolute; top: 21px; height: 44px; display: flex; align-items: center; justify-content: center; font-size: 16px; text-transform: uppercase; }
  .nav-login { left: 917px; width: 77px; border: 3px solid var(--white); color: var(--white); }
  .nav-post { left: 1015px; width: 127px; background: var(--white); color: var(--teal); }

  .hero { position: absolute; left: 0; top: 85px; width: 1200px; height: 526px; text-align: center; color: var(--white); }
  .hero-photo {
    position: absolute; inset: 0;
    background:
      linear-gradient(rgba(20, 16, 12, 0.35), rgba(20, 16, 12, 0.35)),
      radial-gradient(ellipse 14% 22% at 80% 33%, rgba(245, 240, 225, 0.95) 0%, rgba(245, 240, 225, 0) 100%),
      radial-gradient(ellipse 16% 16% at 90% 82%, rgba(235, 225, 205, 0.95) 0%, rgba(235, 225, 205, 0) 100%),
      radial-gradient(ellipse 10% 18% at 64% 30%, rgba(225, 220, 205, 0.8) 0%, rgba(225, 220, 205, 0) 100%),
      radial-gradient(ellipse 22% 14% at 52% 86%, rgba(120, 70, 35, 0.95) 0%, rgba(120, 70, 35, 0) 100%),
      radial-gradient(ellipse 12% 22% at 34% 32%, rgba(40, 32, 28, 0.9) 0%, rgba(40, 32, 28, 0) 100%),
      radial-gradient(ellipse 16% 16% at 8% 80%, rgba(150, 120, 95, 0.9) 0%, rgba(150, 120, 95, 0) 100%),
      linear-gradient(180deg, #d8cdb8 0%, #bfb29a 45%, #8d6c4c 75%, #5a3f2a 100%);
  }
  .hero-title { position: relative; padding-top: 160px; font-size: 57px; font-weight: 400; line-height: 1.2; }
  .hero-copy { position: absolute; left: 0; right: 0; top: 276px; font-size: 24px; line-height: 24px; font-weight: 500; }

  .band { position: absolute; left: 0; width: 1200px; height: 177px; display: flex; align-items: center; justify-content: center; color: var(--white); font-size: 26px; font-weight: 500; text-transform: uppercase; }
  .band-pointer { position: absolute; left: 564px; top: 176px; }
  .band-rooms { top: 611px; background: var(--pink); }
  .band-flatmates { top: 1552px; background: var(--blue); }

  .carousel { position: absolute; left: 0; width: 1200px; height: 570px; }
  .carousel-rooms { top: 886px; }
  .carousel-flatmates { top: 1826px; }
  .slide { position: absolute; left: 46px; top: 0; width: 570px; height: 570px; background: var(--room-photo); }
  .slide-caption { position: absolute; left: 0; bottom: 0; width: 100%; height: 131px; background: var(--shade); color: var(--white); font-size: 26px; font-weight: 500; padding: 26px 0 0 33px; }
  .slide-arrow { position: absolute; top: 239px; width: 70px; height: 70px; }
  .arrow-prev { left: 9px; }
  .arrow-next { left: 583px; }
  .thumb { position: absolute; top: 0; width: 160px; height: 158px; background: var(--room-photo); }
  .thumb-1 { left: 645px; }
  .thumb-2 { left: 819px; width: 161px; }
  .thumb-3 { left: 996px; }
  .description { position: absolute; left: 720px; top: 236px; font-size: 25px; }
</style>
</head>
<body>
  <header class="site-header">
    <div class="brand"><span class="brand-mark"></span><span class="brand-name">LOGO</span></div>
    <span class="nav-button nav-login">Login</span>
    <span class="nav-button nav-post">Post room</span>
  </header>

  <section class="hero">
    <div class="hero-photo" role="img" aria-label="Bright shared living room with sofa, fireplace, lamp and wooden floor"></div>
    <h1 class="hero-title">Find your perfect flatmate</h1>
    <p class="hero-copy">No fees. We don’t charge you anything.<br>That means no fees to post an advert and<br>no fees to contact your potential new flatmate.</p>
  </section>

  <h2 class="band band-rooms">New rooms
    <svg class="band-pointer" width="72" height="30" viewBox="0 0 72 30"><polygon points="0,0 72,0 36,30" fill="#f59195"/></svg>
  </h2>

  <section class="carousel carousel-rooms">
    <div class="slide" role="img" aria-label="Featured room with tall window, pink armchair, lamp and desk">
      <div class="slide-caption">TITLE</div>
    </div>
    <svg class="slide-arrow arrow-prev" viewBox="0 0 70 70"><circle cx="35" cy="35" r="35" fill="var(--arrow-pink)"/><polyline points="39,25 29,35 39,45" fill="none" stroke="#fff" stroke-width="5"/></svg>
    <svg class="slide-arrow arrow-next" viewBox="0 0 70 70"><circle cx="35" cy="35" r="35" fill="var(--arrow-pink)"/><polyline points="31,25 41,35 31,45" fill="none" stroke="#fff" stroke-width="5"/></svg>
    <div class="thumb thumb-1" role="img" aria-label="Room thumbnail"></div>
    <div class="thumb thumb-2" role="img" aria-label="Room thumbnail"></div>
    <div class="thumb thumb-3" role="img" aria-label="Room thumbnail"></div>
    <p class="description">Descriptions</p>
  </section>

  <h2 class="band band-flatmates">New flatmates
    <svg class="band-pointer" width="72" height="30" viewBox="0 0 72 30"><polygon points="0,0 72,0 36,30" fill="#85c8e4"/></svg>
  </h2>

  <section class="carousel carousel-flatmates">
    <div class="slide" role="img" aria-label="Featured flatmate listing room with tall window, pink armchair, lamp and desk">
      <div class="slide-caption">TITLE</div>
    </div>
    <svg class="slide-arrow arrow-prev" viewBox="0 0 70 70"><circle cx="35" cy="35" r="35" fill="var(--arrow-blue)"/><polyline points="39,25 29,35 39,45" fill="none" stroke="#fff" stroke-width="5"/></svg>
    <svg class="slide-arrow arrow-next" viewBox="0 0 70 70"><circle cx="35" cy="35" r="35" fill="var(--arrow-blue)"/><polyline points="31,25 41,35 31,45" fill="none" stroke="#fff" stroke-width="5"/></svg>
    <div class="thumb thumb-1" role="img" aria-label="Flatmate listing thumbnail"></div>
    <div class="thumb thumb-2" role="img" aria-label="Flatmate listing thumbnail"></div>
    <div class="thumb thumb-3" role="img" aria-label="Flatmate listing thumbnail"></div>
    <p class="description">Descriptions</p>
  </section>
</body>
</html>
```